Ethics in the Workplace City of Brellmoor California, USA

This a presentation on Ethics in the workplace, specifically for code enforcement department staff in Brellmoor California. The content of the presentation should follow the agenda outline. This is revised presentaton used for lower left staff, however, managers have specifics they want to be covered in the briefing. I have provided a separate document where need to explain where new slides and graphics should be inserted to emphasis the message the clients want communicated. I need some of my slides revamped to include better graphics of the content that I am presenting. The PPT attached is only to show the color and theme that city of Brellmoor Code Enforcement want. I will need some blank slides in case I need to add content. The slides must be number and editable, please do not paste a picture in the ppt. I must be able to change if needed without having to come back to the free lancer

Target Market(s)

City of Brellmoor Oregon Code Enforcement Department Staff especially code enforcement officers

Industry/Entity Type

Municipal Government City Goverment

Colors
00AB8E
00BBA5
67D7C9
C6EFE9
E9F9F6

Requirements
Must have
• Ethics, honest, integrity, cultural competencies, diversity, workplace behavior, ethics policy implementing an ethics program . I have attached the must haves
Nice to have
• Graphics per the recommendations per the slides
Should not have
• Discriminationatry language, feminist graphics offensive or insensitve language

```html
<!DOCTYPE html>
<html lang="en">
<head>
<meta charset="utf-8">
<title>Ethics in the Workplace – City of Brellmoor</title>
<link href="https://fonts.googleapis.com/css2?family=Lato:wght@400;700&family=Source+Serif+4:wght@600;700&display=swap" rel="stylesheet">
<style>
:root{
  --stage:#222222;
  --blue:#1b479f;
  --gold:#b58a52;
  --ink:#1c1c1c;
  --body:#2b2b2b;
  --paper:#ffffff;
  --mist:#f3f4f8;
}
*{margin:0;padding:0;box-sizing:border-box}
html,body{width:1200px;height:4110px;overflow:hidden;background:var(--stage)}
body{position:relative;font-family:"Lato",sans-serif;color:var(--body)}
.slide{position:absolute;left:53px;width:1096px;height:616px;background:var(--paper);overflow:hidden}
.abs{position:absolute}
.brand{position:absolute;display:flex;align-items:center;gap:8px;font-family:"Source Serif 4",serif;font-weight:700;font-size:30px;color:var(--blue);letter-spacing:.5px}
.brand .dot{width:18px;height:18px;border-radius:50%;background:var(--gold)}
.title{position:absolute;font-family:"Source Serif 4",serif;font-weight:700;color:var(--blue);font-size:33px;line-height:45px}
.rule{position:absolute;height:2px;background:var(--gold)}
.rule::after{content:"";position:absolute;right:-3px;top:-3px;width:8px;height:8px;border-radius:50%;background:var(--gold)}
.subhead{position:absolute;font-family:"Source Serif 4",serif;font-weight:700;color:var(--ink);font-size:23px;line-height:33px}
.tagline{position:absolute;font-size:19px;color:var(--ink)}
.para{position:absolute;font-size:15px;line-height:28px;color:var(--body)}
.photo{position:absolute}
.icon{width:30px;height:30px;border-radius:50%;background:var(--gold);display:flex;align-items:center;justify-content:center;flex:none}
.contact{position:absolute;display:flex;gap:12px;align-items:flex-start}
.contact b{display:block;font-size:15px;color:var(--ink)}
.contact span{font-size:13px;color:var(--body);line-height:22px}
/* agenda */
.agenda-col{position:absolute;top:100px}
.agenda-col h3{font-weight:400;color:var(--gold);font-size:18px;line-height:27px;margin-bottom:2px}
.agenda-col ul{list-style:none;margin-bottom:8px}
.agenda-col li{position:relative;padding-left:20px;font-size:15px;line-height:20px;margin-bottom:9px;color:var(--body)}
.agenda-col li::before{content:"";position:absolute;left:2px;top:7px;width:7px;height:7px;border-top:2px solid var(--gold);border-right:2px solid var(--gold);transform:rotate(45deg)}
.thanks-contact{position:absolute;display:flex;gap:14px;align-items:flex-start}
.thanks-contact b{display:block;font-family:"Source Serif 4",serif;font-size:22px;color:var(--ink);font-weight:700}
.thanks-contact span{font-size:16px;line-height:28px;color:var(--body)}
.thanks-contact .icon{width:38px;height:38px;margin-top:24px}
</style>
</head>
<body>

<!-- Title slide -->
<section class="slide" style="top:53px">
  <div class="brand" style="left:59px;top:40px"><span class="dot"></span>Brellmoor</div>
  <h1 class="title" style="left:54px;top:178px">ETHICS IN THE WORKPLACE</h1>
  <div class="rule" style="left:0;top:239px;width:123px"></div>
  <div class="abs" style="left:54px;top:268px;font-family:'Source Serif 4',serif;font-weight:700;color:var(--gold);font-size:21px">PRESENTED BY:</div>
  <div class="abs" style="left:54px;top:316px;font-size:16px;font-weight:700;color:var(--ink)">DANA WHITFIELD (SHE, HER, HERS) &nbsp;|&nbsp; MARCUS ELLERY J.D (HE/HIM)</div>
  <div class="abs" style="left:54px;top:364px;font-size:18px;color:var(--gold);font-weight:700">NORTHGATE LEARNING ACADEMY</div>
  <div class="contact" style="left:54px;top:405px">
    <div class="icon"><svg width="14" height="11" viewBox="0 0 14 11"><rect x="0.5" y="0.5" width="13" height="10" fill="none" stroke="#fff"/><path d="M0.5 0.5 7 6 13.5 0.5" fill="none" stroke="#fff"/></svg></div>
    <div><b>Email Us:</b><span>contact@northgatelearning.org</span></div>
  </div>
  <div class="contact" style="left:54px;top:475px">
    <div class="icon"><svg width="14" height="14" viewBox="0 0 24 24"><path fill="#fff" d="M6.6 10.8a15 15 0 0 0 6.6 6.6l2.2-2.2c.3-.3.7-.4 1-.2 1.1.4 2.3.6 3.6.6.6 0 1 .4 1 1V20c0 .6-.4 1-1 1A17 17 0 0 1 3 4c0-.6.4-1 1-1h3.5c.6 0 1 .4 1 1 0 1.3.2 2.5.6 3.6.1.3 0 .7-.2 1z"/></svg></div>
    <div><b>Phone Number:</b><span>(503) 555-0147</span></div>
  </div>
  <div class="photo" role="img" aria-label="Photo of smiling colleagues working together at a laptop in a bright office" style="left:560px;top:-110px;width:660px;height:660px;border-radius:50%;border:12px solid var(--gold);border-top-color:transparent;border-right-color:transparent;background:linear-gradient(135deg,#e7ebef,#c9b8a3 55%,#6f7f8f)"></div>
</section>

<!-- Agenda -->
<section class="slide" style="top:724px;background:linear-gradient(135deg,var(--paper),var(--mist))">
  <h2 class="title" style="left:54px;top:24px">AGENDA</h2>
  <div class="rule" style="left:0;top:78px;width:123px"></div>
  <div class="brand" style="left:921px;top:30px"><span class="dot"></span>Brellmoor</div>
  <div class="agenda-col" style="left:54px;width:330px">
    <h3>1) INTRODUCTION</h3>
    <ul><li>Welcome and introductions</li><li>Explanation of the importance of ethics in the workplace</li><li>Brief overview of the presentation</li></ul>
    <h3>2) UNDERSTANDING ETHICS</h3>
    <ul><li>Definition of ethics</li><li>The role of ethics in the workplace</li><li>Different ethical frameworks</li></ul>
    <h3>3) TYPES OF WORKPLACE<br>ETHICS VIOLATIONS</h3>
    <ul><li>Discrimination and harassment</li><li>Fraud and misrepresentation</li><li>Insider trading</li><li>Environmental violations</li><li>Other types of ethics violations</li></ul>
  </div>
  <div class="agenda-col" style="left:420px;width:320px">
    <h3>4) CONSEQUENCES OF ETHICS VIOLATIONS</h3>
    <ul><li>Legal consequences</li><li>Reputational damage</li><li>Financial Consequences</li><li>Impact on employees</li></ul>
    <h3>5) &nbsp;IMPLEMENTING ETHICAL PRACTICES</h3>
    <ul><li>Developing a code of conduct</li><li>Training employees on ethical behavior</li><li>Encouraging reporting of ethics violations</li><li>Creating an ethical culture</li></ul>
    <h3>5) &nbsp;CASE STUDIES AND<br>DISCUSSION</h3>
    <ul style="width:470px"><li>Real-life examples of workplace ethics violations</li><li>Discussion of how to prevent and address these violations.</li><li>Q&amp;A session</li></ul>
  </div>
  <div class="agenda-col" style="left:745px;width:320px">
    <h3>4) CONCLUSION</h3>
    <ul><li>Recap of critical points</li><li>Final thoughts and recommendations</li><li>Call to Action</li></ul>
  </div>
</section>

<!-- Purpose -->
<section class="slide" style="top:1393px">
  <div class="abs" style="left:793px;top:0;width:303px;height:616px;background:var(--gold)"></div>
  <div class="brand" style="left:54px;top:32px"><span class="dot"></span>Brellmoor</div>
  <h2 class="title" style="left:54px;top:130px">PURPOSE OF DEVELOPING A<br>CODE OF ETHICS VISUAL:</h2>
  <div class="rule" style="left:0;top:235px;width:123px"></div>
  <h3 class="subhead" style="left:54px;top:254px">PURPOSE OF DEVELOPING A CODE OF<br>ETHICS</h3>
  <div class="tagline" style="left:54px;top:336px">Guiding Principles for Ethical Conduct</div>
  <p class="para" style="left:54px;top:370px;width:480px">A code of ethics serves as a compass, providing clear guidance and principles for ethical conduct within the code enforcement profession.</p>
  <p class="para" style="left:54px;top:453px;width:480px">It promotes integrity, professionalism, and accountability, fostering a culture of ethical decision-making and community trust.</p>
  <div class="photo" role="img" aria-label="Photo of two professionals shaking hands in a modern office" style="left:634px;top:69px;width:410px;height:478px;border-radius:0 40px 40px 0;background:linear-gradient(160deg,#cfd9e2,#8c9aa6 50%,#2f3338)"></div>
  <div class="photo" role="img" aria-label="Photo of a compass on a turquoise background" style="left:557px;top:362px;width:186px;height:183px;border:4px solid #fff;background:radial-gradient(circle,#3b5560 0 30%,#9fe3dd 32%,#7fd7d2)"></div>
</section>

<!-- Group exercises -->
<section class="slide" style="top:2078px;background:linear-gradient(135deg,var(--paper),var(--mist))">
  <div class="photo" role="img" aria-label="Photo of a team of colleagues discussing around a laptop" style="left:51px;top:80px;width:417px;height:484px;border:5px solid var(--gold);border-radius:40px;background:linear-gradient(160deg,#e6e9ec,#b9ab9a 55%,#4b4a4c)"></div>
  <div class="brand" style="left:921px;top:29px"><span class="dot"></span>Brellmoor</div>
  <h2 class="title" style="left:568px;top:106px">GROUP EXERCISES OR<br>BREAKOUT SESSIONS VISUAL</h2>
  <div class="rule" style="left:469px;top:211px;width:171px"></div>
  <h3 class="subhead" style="left:568px;top:230px">GROUP EXERCISES OR BREAKOUT<br>SESSIONS</h3>
  <div class="tagline" style="left:568px;top:312px">Active Engagement in Ethical Development</div>
  <p class="para" style="left:568px;top:348px;width:490px">Engaging in group exercises or breakout sessions allows us to collectively explore and define the fundamental ethical principles and behaviors that will guide our code enforcement personnel.</p>
  <p class="para" style="left:568px;top:458px;width:490px">These interactive sessions promote active learning, shared perspectives, and the development of a code of ethics that reflects our department's unique challenges and values.</p>
</section>

<!-- Displaying the code -->
<section class="slide" style="top:2748px">
  <div class="abs" style="left:0;top:0;width:303px;height:616px;background:var(--blue)"></div>
  <div class="photo" role="img" aria-label="Photo of wooden blocks printed with ethics icons stacked into steps" style="left:56px;top:69px;width:408px;height:479px;border-radius:40px;background:linear-gradient(160deg,#e3efea,#cdbb9c 60%,#a88c62)"></div>
  <div class="brand" style="left:921px;top:29px"><span class="dot"></span>Brellmoor</div>
  <h2 class="title" style="left:568px;top:130px">DISPLAYING THE CODE OF<br>ETHICS VISUAL</h2>
  <div class="rule" style="left:466px;top:233px;width:174px"></div>
  <h3 class="subhead" style="left:568px;top:256px">OUR CODE OF ETHICS</h3>
  <div class="tagline" style="left:568px;top:302px">Our Commitment to Ethical Excellence</div>
  <p class="para" style="left:568px;top:341px;width:490px">After collaborative discussions and thoughtful considerations, we have developed our department's code of ethics.</p>
  <p class="para" style="left:568px;top:424px;width:490px">This code embodies our shared values, guiding principles, and the standards of conduct we uphold as code enforcement professionals. Let's review and embrace our code of ethics as the foundation of our ethical journey.</p>
</section>

<!-- Thank you -->
<section class="slide" style="top:3422px;height:619px;background:linear-gradient(160deg,#f6f7fa,#dde2ea 60%,#eef0f4)">
  <div class="brand" style="left:0;width:1096px;justify-content:center;top:160px"><span class="dot"></span>Brellmoor</div>
  <h2 class="title" style="left:0;width:1096px;text-align:center;top:260px;font-size:48px;line-height:60px">THANK YOU</h2>
  <div class="thanks-contact" style="left:52px;top:350px">
    <div class="icon"><svg width="14" height="18" viewBox="0 0 14 18"><path fill="#fff" d="M7 0a7 7 0 0 0-7 7c0 5 7 11 7 11s7-6 7-11a7 7 0 0 0-7-7zm0 9.5A2.5 2.5 0 1 1 7 4.5a2.5 2.5 0 0 1 0 5z"/></svg></div>
    <div><b>Address:</b><span>City of Brellmoor, Oregon<br>United States</span></div>
  </div>
  <div class="thanks-contact" style="left:427px;top:354px">
    <div class="icon"><svg width="16" height="12" viewBox="0 0 14 11"><rect x="0.5" y="0.5" width="13" height="10" fill="none" stroke="#fff"/><path d="M0.5 0.5 7 6 13.5 0.5" fill="none" stroke="#fff"/></svg></div>
    <div><b>Email Us:</b><span>contact@northgatelearning.org</span></div>
  </div>
  <div class="thanks-contact" style="left:823px;top:354px">
    <div class="icon"><svg width="16" height="16" viewBox="0 0 24 24"><path fill="#fff" d="M6.6 10.8a15 15 0 0 0 6.6 6.6l2.2-2.2c.3-.3.7-.4 1-.2 1.1.4 2.3.6 3.6.6.6 0 1 .4 1 1V20c0 .6-.4 1-1 1A17 17 0 0 1 3 4c0-.6.4-1 1-1h3.5c.6 0 1 .4 1 1 0 1.3.2 2.5.6 3.6.1.3 0 .7-.2 1z"/></svg></div>
    <div><b>Phone Number:</b><span>(503) 555-0147</span></div>
  </div>
</section>

</body>
</html>
```